Business Card Design for Kidvale (Hires out childrens play areas)

Looking to have a business card designed for a company we just bought. The company rents out childrens play areas.

I have uploaded a couple of examples of the kind of business card style I like. Here are two more examples:

https://quorvastudio.nz/project/bright-romp-branding/
https://imgvaultcdn.com/design_img/8841052/302917/302917_5518203_8841052_b73e19a2_image.jpg

I think a white card will be best due to all the colours in the logo.

Size we require: 3.75" x 2.25" (horizontally orientated) with a 0.125" bleed

Uploaded is two versions of our logo.

Details for the card:
1. My name: Liam Verster
2. Title: Managing Director
3. Phone no: 021 563 417
4. Email: liam@kidvale.co.nz
5. URL: www.kidvale.co.nz
6. Address:
PO Box 318625
Fernlea, Auckland

Let me know if you need anything else.

Target Market(s)

Hospitals, doctors surgeries, bed shops, etc.

Contact Information for Business Card

Details for the card:
1. My name: Liam Verster
3. Phone no: 021 563 417
5. URL: www.kidvale.co.nz
6. Address:
PO Box 318625
Fernlea, Auckland

Requirements
Should not have
• Not too busy.

```html
<!DOCTYPE html>
<html lang="en">
<head>
<meta charset="utf-8">
<title>Kidvale Business Card</title>
<link href="https://fonts.googleapis.com/css2?family=Lato:wght@400;700&display=swap" rel="stylesheet">
<style>
  :root {
    --page-bg: #3a3a3c;
    --card-bg: #121213;
    --card-bg-edge: #1c1c1e;
    --brand-blue: #1560c4;
    --text-light: #e6e6e6;
    --text-muted: #b9b9b9;
    --divider: #8a8a8a;
  }
  * { box-sizing: border-box; margin: 0; padding: 0; }
  html, body {
    width: 1200px;
    height: 900px;
    overflow: hidden;
  }
  body {
    background: var(--page-bg);
    font-family: "Lato", sans-serif;
    display: flex;
    flex-direction: column;
    align-items: center;
    justify-content: center;
    gap: 50px;
  }
  .card {
    position: relative;
    width: 625px;
    height: 375px;
    background: radial-gradient(ellipse at 40% 30%, var(--card-bg-edge), var(--card-bg) 70%);
    overflow: hidden;
  }
  .card__band {
    position: absolute;
    left: 0;
    right: 0;
    bottom: 0;
    height: 9px;
    background: var(--brand-blue);
  }

  /* Front */
  .card--front {
    display: flex;
    align-items: center;
    justify-content: center;
  }
  .brand {
    display: flex;
    align-items: center;
    gap: 16px;
    margin-bottom: 10px;
  }
  .brand__dot {
    width: 34px;
    height: 34px;
    border-radius: 50%;
    background: var(--brand-blue);
  }
  .brand__name {
    font-size: 54px;
    font-weight: 700;
    color: var(--text-light);
    letter-spacing: 1px;
  }

  /* Back */
  .contact {
    position: absolute;
    left: 150px;
    top: 118px;
    display: flex;
    align-items: stretch;
  }
  .person {
    text-align: right;
    padding-right: 26px;
    padding-top: 8px;
  }
  .person__name {
    font-size: 21px;
    font-weight: 400;
    color: var(--brand-blue);
    text-transform: uppercase;
    letter-spacing: 0.5px;
  }
  .person__title {
    font-size: 16px;
    color: var(--text-muted);
    margin-top: 2px;
  }
  .contact__divider {
    width: 1px;
    height: 76px;
    background: var(--divider);
  }
  .details {
    list-style: none;
    padding-left: 22px;
    padding-top: 6px;
  }
  .details__item {
    display: flex;
    align-items: center;
    gap: 10px;
    font-size: 16px;
    color: var(--text-light);
    height: 24px;
  }
  .details__icon {
    width: 18px;
    height: 18px;
    flex: none;
  }
  .address {
    position: absolute;
    left: 170px;
    top: 265px;
    font-size: 16px;
    color: var(--text-light);
    word-spacing: 1px;
  }
</style>
</head>
<body>

  <section class="card card--front" aria-label="Card front">
    <div class="brand">
      <span class="brand__dot"></span>
      <span class="brand__name">Kidvale</span>
    </div>
    <div class="card__band"></div>
  </section>

  <section class="card card--back" aria-label="Card back">
    <div class="contact">
      <div class="person">
        <p class="person__name">Liam Verster</p>
        <p class="person__title">Managing Director</p>
      </div>
      <div class="contact__divider"></div>
      <ul class="details">
        <li class="details__item">
          <svg class="details__icon" viewBox="0 0 18 18" aria-hidden="true">
            <circle cx="9" cy="9" r="9" fill="var(--brand-blue)"/>
            <path d="M6.2 4.6l1.4 1.6-.7 1.2c.5 1.2 1.3 2 2.5 2.5l1.2-.7 1.6 1.4-.8 1.5c-3.2-.3-6.2-3.3-6.5-6.5z" fill="#121213"/>
          </svg>
          <span>021 563 417</span>
        </li>
        <li class="details__item">
          <svg class="details__icon" viewBox="0 0 18 18" aria-hidden="true">
            <circle cx="9" cy="9" r="9" fill="var(--brand-blue)"/>
            <rect x="4.5" y="6" width="9" height="6.2" fill="#121213"/>
            <path d="M4.7 6.2L9 9.6l4.3-3.4" fill="none" stroke="var(--brand-blue)" stroke-width="0.9"/>
          </svg>
          <span>liam@kidvale.co.nz</span>
        </li>
        <li class="details__item">
          <svg class="details__icon" viewBox="0 0 18 18" aria-hidden="true">
            <circle cx="9" cy="9" r="9" fill="var(--brand-blue)"/>
            <circle cx="9" cy="9" r="4.4" fill="none" stroke="#121213" stroke-width="1.1"/>
            <ellipse cx="9" cy="9" rx="1.9" ry="4.4" fill="none" stroke="#121213" stroke-width="1"/>
            <line x1="4.6" y1="9" x2="13.4" y2="9" stroke="#121213" stroke-width="1"/>
          </svg>
          <span>www.kidvale.co.nz</span>
        </li>
      </ul>
    </div>
    <p class="address">PO Box 318625&nbsp; Fernlea, Auckland</p>
    <div class="card__band"></div>
  </section>

</body>
</html>
```